RV park billboard

We need a billboard for cedar bend RV park . I was thinking about having a big orange in the background. We will have free fiber optic internet and each camper will have its own personal hotspot and we want that on the sign... Also the phone number with the area code... But I don't have the exact number yet. Size of sign will be 12 x 40
Make sure sign has Cedar Bend RV park on it
Plant turnaround workers

```html
<!DOCTYPE html>
<html lang="en">
<head>
<meta charset="utf-8">
<title>Cedar Bend RV park billboard</title>
<link href="https://fonts.googleapis.com/css2?family=Rubik:wght@400;700&display=swap" rel="stylesheet">
<style>
  :root {
    --page-bg: #eef2f6;
    --sign-white: #ffffff;
    --orange-top: #f7931e;
    --orange-bottom: #f26522;
    --fruit-light: #f7901e;
    --fruit-dark: #df7a3a;
    --leaf-green: #8dc63f;
    --text-white: #ffffff;
  }
  html, body {
    margin: 0;
    width: 1200px;
    height: 815px;
    overflow: hidden;
    background: var(--page-bg);
  }
  .canvas {
    width: 1200px;
    height: 815px;
    display: flex;
    align-items: center;
    justify-content: center;
  }
  .billboard {
    display: block;
    width: 1200px;
    height: 360px;
  }
  .billboard-title {
    font-family: "Rubik", sans-serif;
    font-weight: 700;
    font-size: 62px;
    fill: var(--text-white);
  }
  .feature-heading {
    font-family: "Rubik", sans-serif;
    font-weight: 700;
    font-size: 33px;
    fill: var(--text-white);
  }
  .feature-detail {
    font-family: "Rubik", sans-serif;
    font-weight: 400;
    font-size: 28px;
    letter-spacing: 1px;
    fill: var(--text-white);
  }
  .phone-number {
    font-family: "Rubik", sans-serif;
    font-weight: 700;
    font-size: 46px;
    fill: var(--text-white);
  }
</style>
</head>
<body>
<main class="canvas">
  <svg class="billboard" viewBox="0 0 1134 340" xmlns="http://www.w3.org/2000/svg" aria-label="Cedar Bend RV park billboard">
    <defs>
      <linearGradient id="orange-panel" x1="0" y1="0" x2="0" y2="1">
        <stop offset="0" stop-color="var(--orange-top)"/>
        <stop offset="1" stop-color="var(--orange-bottom)"/>
      </linearGradient>
      <radialGradient id="fruit-fill" cx="0.55" cy="0.5" r="0.6">
        <stop offset="0" stop-color="var(--fruit-light)"/>
        <stop offset="1" stop-color="var(--fruit-dark)"/>
      </radialGradient>
    </defs>

    <rect class="sign-base" width="1134" height="340" fill="var(--sign-white)"/>

    <path class="orange-panel" d="M330 0 H1134 V340 H470 C520 280 530 150 460 80 C420 40 380 18 330 0 Z" fill="url(#orange-panel)"/>

    <path class="phone-band" d="M0 249 H502 C498 275 490 300 480 321 H0 Z" fill="var(--leaf-green)"/>

    <rect class="fruit-illustration" x="72" y="18" width="302" height="222" rx="100" fill="url(#fruit-fill)" role="img" aria-label="Illustration of two oranges with green leaves"/>

    <text class="billboard-title" x="1118" y="68" text-anchor="end">Cedar Bend RV park</text>

    <g class="wifi-icon" fill="none" stroke="var(--text-white)" stroke-width="6" stroke-linecap="round">
      <path d="M530 150 A46 46 0 0 1 596 150"/>
      <path d="M541 162 A30 30 0 0 1 585 162"/>
      <path d="M552 174 A15 15 0 0 1 574 174"/>
      <circle cx="563" cy="185" r="3" fill="var(--text-white)"/>
    </g>
    <text class="feature-heading" x="640" y="157">Personal hotspot</text>
    <text class="feature-detail" x="640" y="194">for each camper</text>

    <g class="fiber-icon" stroke="var(--text-white)" stroke-width="3" fill="var(--text-white)">
      <rect x="556" y="274" width="18" height="28" stroke="none"/>
      <path d="M565 274 V240 M560 274 L546 252 M570 274 L582 253" fill="none"/>
      <circle cx="565" cy="238" r="4" stroke="none"/>
      <circle cx="545" cy="250" r="4" stroke="none"/>
      <circle cx="583" cy="251" r="4" stroke="none"/>
    </g>
    <text class="feature-heading" x="642" y="262">Free fiber optic</text>
    <text class="feature-detail" x="642" y="299">internet</text>

    <text class="phone-number" x="45" y="301">(409) 555-0172</text>
  </svg>
</main>
</body>
</html>
```